Vantrel Consulting Business card design.

See our website www.vantrelconsulting.com which will give you a good idea of what we are about. The font is called 'Play'.

I'd like a standout business card in keeping with the themes and branding on the website

Target Market(s)

professionals. HR directors

Industry/Entity Type

Business

Contact Information for Business Card

Vantrel Consulting PO Box 3917 Marrowdene NSW 2279 1300 584 316 Gareth Lindqvane Principal email: career@vantrelconsulting.com ABN: 41293087614

Other font styles liked:
• Play

Requirements
Must have
• Must have same design colours and branding as website.
• On back I'd prefer a list of the things we do which appears below the name at the header on the website

```html
<!DOCTYPE html>
<html lang="en">
<head>
<meta charset="utf-8">
<title>Vantrel Consulting – Business Card</title>
<link rel="stylesheet" href="https://fonts.googleapis.com/css2?family=Play:wght@400;700&display=swap">
<style>
  :root {
    --navy-deep: #0b2236;
    --navy: #163a57;
    --navy-mid: #1f4a6b;
    --sky: #1f7fd6;
    --sky-light: #7fc3f3;
    --accent: #2bb3e8;
    --accent-dark: #1a7fb8;
    --paper: #f3f5f7;
    --ink: #1d3550;
    --ink-soft: #4a5d70;
    --stage: #e6e8eb;
  }
  * { box-sizing: border-box; margin: 0; padding: 0; }
  html, body {
    width: 1200px; height: 902px; overflow: hidden;
    background: var(--stage);
    font-family: 'Play', sans-serif;
  }
  .canvas {
    position: relative; width: 1200px; height: 902px;
  }
  .card {
    position: absolute; left: 250px; width: 700px; height: 400px;
    overflow: hidden; border-radius: 4px;
    box-shadow: 0 6px 18px rgba(0,0,0,0.18);
  }
  .card--front { top: 34px; }
  .card--back { top: 468px; background: var(--paper); }

  /* front */
  .hero-photo {
    position: absolute; inset: 0 0 120px 0;
    background:
      linear-gradient(160deg, transparent 55%, rgba(255,255,255,0.85) 72%, #e9f2fa 85%),
      linear-gradient(180deg, var(--sky) 0%, #3f9be6 55%, var(--sky-light) 100%);
  }
  .front-band {
    position: absolute; left: 0; right: 0; bottom: 0; height: 120px;
    background: linear-gradient(180deg, var(--navy-deep) 0%, var(--navy) 100%);
  }
  .brand-name {
    font-family: 'Play', sans-serif; font-weight: 700;
    color: #ffffff; letter-spacing: 1px; text-transform: uppercase;
    white-space: nowrap;
  }
  .services {
    font-family: 'Play', sans-serif; color: var(--accent);
    letter-spacing: 0.5px; white-space: nowrap;
  }
  .front-band .brand-name { position: absolute; left: 150px; top: 22px; font-size: 44px; }
  .front-band .services { position: absolute; left: 152px; top: 78px; font-size: 14px; }

  /* back */
  .back-shapes { position: absolute; inset: 0; }
  .back-header .brand-name { position: absolute; left: 120px; top: 98px; font-size: 46px; }
  .back-header .services { position: absolute; left: 122px; top: 158px; font-size: 15px; }
  .holder { position: absolute; left: 44px; top: 300px; color: var(--ink); }
  .holder-name { font-size: 31px; font-weight: 700; letter-spacing: 0.3px; }
  .holder-title { font-size: 21px; color: var(--ink-soft); margin-top: 2px; }
  .divider {
    position: absolute; left: 388px; top: 282px; width: 1px; height: 96px;
    background: var(--ink-soft);
  }
  .contact { position: absolute; left: 406px; top: 278px; color: var(--ink); font-size: 15px; }
  .contact-abn { font-size: 17px; margin-bottom: 8px; }
  .contact-row { display: flex; align-items: center; gap: 9px; height: 24px; }
  .contact-icon { width: 15px; height: 15px; flex: none; }
</style>
</head>
<body>
<main class="canvas">

  <section class="card card--front" aria-label="Card front">
    <div class="hero-photo" role="img" aria-label="Photo of a snowboarder mid-air above a snowy mountain peak against a deep blue sky"></div>
    <div class="front-band">
      <div class="brand-name">Vantrel Consulting</div>
      <div class="services">Search &amp; Select | Career | Coaching | Leadership | Outplacement</div>
    </div>
  </section>

  <section class="card card--back" aria-label="Card back">
    <svg class="back-shapes" width="700" height="400" viewBox="0 0 700 400" aria-hidden="true">
      <defs>
        <linearGradient id="headerFill" x1="0" y1="0" x2="1" y2="1">
          <stop offset="0" stop-color="#1f4a6b"/>
          <stop offset="0.6" stop-color="#0f2c45"/>
          <stop offset="1" stop-color="#0b2236"/>
        </linearGradient>
      </defs>
      <polygon points="0,0 700,0 700,118 660,236 40,236 0,236" fill="url(#headerFill)"/>
      <polygon points="0,236 660,236 700,118 700,132 668,248 60,248 0,248" fill="#2bb3e8"/>
      <polygon points="60,248 668,248 660,256 70,256" fill="#1a7fb8"/>
    </svg>
    <div class="back-header">
      <div class="brand-name">Vantrel Consulting</div>
      <div class="services">Search &amp; Select | Career | Coaching | Leadership | Outplacement</div>
    </div>
    <div class="holder">
      <div class="holder-name">Gareth Lindqvane</div>
      <div class="holder-title">Principal</div>
    </div>
    <div class="divider"></div>
    <div class="contact">
      <div class="contact-abn">ABN: 41293087614</div>
      <div class="contact-row">
        <svg class="contact-icon" viewBox="0 0 16 16" aria-hidden="true"><rect x="1" y="1" width="14" height="14" rx="2" fill="#1d3550"/><path d="M5 4h2l1 3-1.5 1a6 6 0 0 0 2.5 2.5L10 9l3 1v2a1 1 0 0 1-1 1A9 9 0 0 1 4 5a1 1 0 0 1 1-1z" fill="#fff"/></svg>
        <span>1300 584 316</span>
      </div>
      <div class="contact-row">
        <svg class="contact-icon" viewBox="0 0 16 16" aria-hidden="true"><rect x="1" y="1" width="14" height="14" rx="2" fill="#1d3550"/><rect x="4" y="5" width="8" height="6" fill="#fff"/><path d="M4 5l4 3.5L12 5" stroke="#1d3550" stroke-width="1" fill="none"/></svg>
        <span>career@vantrelconsulting.com</span>
      </div>
      <div class="contact-row">
        <svg class="contact-icon" viewBox="0 0 16 16" aria-hidden="true"><rect x="1" y="1" width="14" height="14" rx="2" fill="#1d3550"/><path d="M8 3a3 3 0 0 0-3 3c0 2.5 3 6 3 6s3-3.5 3-6a3 3 0 0 0-3-3z" fill="#fff"/><circle cx="8" cy="6" r="1.1" fill="#1d3550"/></svg>
        <span>PO Box 3917 Marrowdene NSW 2279</span>
      </div>
    </div>
  </section>

</main>
</body>
</html>
```